Business Report Cover

We need a revamped quarterly report cover to send to our clients. We asset manage commercial and residential properties throughout the the United States. We use a .pdf version of a cover that we've used for years but would like a fresh updated look for 2018. The cover should include our company logo (KVL Holdings) and a photo of the property as well as the Quarter/Year of the report.

Industry/Entity Type

Business

```html
<!DOCTYPE html>
<html lang="en">
<head>
<meta charset="utf-8">
<title>Quarterly Operating Report – 1st Quarter 2018 – KVL Holdings</title>
<link rel="stylesheet" href="https://fonts.googleapis.com/css2?family=Montserrat:wght@400;600;700;800&display=swap">
<style>
  :root {
    --backdrop: #d9d9d9;
    --paper: #ffffff;
    --brand-green: #1f7a3d;
    --ink: #141414;
    --ink-soft: #2a2a2a;
    --sky-top: #8fb1d8;
    --sky-mid: #dfe6ee;
    --foliage: #4a5a3a;
    --asphalt: #3b3d40;
    --white: #ffffff;
  }
  * { box-sizing: border-box; margin: 0; padding: 0; }
  html, body {
    width: 1200px;
    height: 1000px;
    overflow: hidden;
    background: var(--backdrop);
    font-family: "Montserrat", sans-serif;
  }
  .cover {
    position: absolute;
    left: 270px;
    top: 50px;
    width: 680px;
    height: 900px;
    background: var(--paper);
    box-shadow: 0 10px 30px rgba(0, 0, 0, 0.18);
    overflow: hidden;
  }
  .property-photo {
    position: absolute;
    left: 0;
    top: 0;
    width: 680px;
    height: 430px;
    background: linear-gradient(180deg,
      var(--sky-top) 0%,
      var(--sky-mid) 28%,
      #c9ccc8 44%,
      var(--foliage) 58%,
      #5a4a44 66%,
      var(--asphalt) 76%,
      #2f3133 100%);
  }
  .property-address {
    position: absolute;
    top: 14px;
    right: 20px;
    text-align: right;
    font-size: 9.5px;
    font-weight: 700;
    line-height: 1.3;
    letter-spacing: 0.04em;
    text-transform: uppercase;
    color: var(--ink-soft);
  }
  .report-title {
    position: absolute;
    left: 0;
    right: 0;
    top: 300px;
    text-align: center;
    color: var(--white);
    text-transform: uppercase;
  }
  .report-title h1 {
    font-size: 27px;
    font-weight: 800;
    line-height: 1.05;
    letter-spacing: 0.01em;
  }
  .report-title .quarter {
    display: block;
    margin-top: 4px;
    font-size: 19px;
    font-weight: 400;
    letter-spacing: 0.03em;
  }
  .year-band {
    position: absolute;
    left: 0;
    top: 430px;
    width: 680px;
    height: 82px;
    background: var(--brand-green);
    display: flex;
    align-items: center;
    justify-content: center;
    color: var(--white);
    font-size: 42px;
    font-weight: 600;
    letter-spacing: 0.02em;
  }
  .company-name {
    position: absolute;
    left: 0;
    right: 0;
    top: 660px;
    display: flex;
    align-items: center;
    justify-content: center;
    gap: 16px;
  }
  .company-name .mark {
    width: 22px;
    height: 22px;
    background: var(--brand-green);
  }
  .company-name span {
    font-size: 52px;
    font-weight: 800;
    color: var(--ink);
    letter-spacing: -0.01em;
  }
</style>
</head>
<body>
  <main class="cover">
    <div class="property-photo" role="img" aria-label="Photograph of the Lakeview Corner Market property: convenience store and fuel canopy with trees and parking lot under a partly cloudy sky"></div>
    <address class="property-address">
      Lakeview Corner Market<br>
      4120 NE Harbor Point Dr.<br>
      Lakeview, WA 98600
    </address>
    <div class="report-title">
      <h1>Quarterly<br>Operating Report</h1>
      <span class="quarter">1st Quarter</span>
    </div>
    <div class="year-band">2018</div>
    <div class="company-name">
      <div class="mark"></div>
      <span>KVL Holdings</span>
    </div>
  </main>
</body>
</html>
```